Design a business card
Business name: Larkspur Yield Advisory
Improving Business Profitibility

- An Overview of the Business & Service:

Business Performance Consulting

- The Target Market: Small to medium-sized business

- Design Specifics:
White card, blue ink, moon eclipse

No Logo

Target Market(s)

Small to medium-sized business

Font styles to use
Sans Serif

```html
<!DOCTYPE html>
<html lang="en">
<head>
<meta charset="utf-8">
<title>Larkspur Yield Advisory – Business Card</title>
<link rel="stylesheet" href="https://fonts.googleapis.com/css2?family=Mulish:ital,wght@0,400;0,600;0,700;1,700&display=swap">
<style>
  :root {
    --ink-blue: #1d73c4;
    --ink-blue-deep: #1566b3;
    --band-grey: #e6e7e9;
    --card-white: #ffffff;
    --backdrop: #eef0f3;
  }
  html, body {
    margin: 0;
    width: 1200px;
    height: 900px;
    overflow: hidden;
    background: var(--backdrop);
    font-family: "Mulish", sans-serif;
  }
  .card {
    position: absolute;
    left: 150px;
    top: 193px;
    width: 900px;
    height: 514px;
    background: var(--card-white);
    box-shadow: 0 10px 30px rgba(0,0,0,0.15);
    overflow: hidden;
  }
  .brand-band {
    position: absolute;
    left: 0; top: 0;
    width: 100%; height: 72px;
    background: var(--ink-blue);
  }
  .brand-name {
    position: absolute;
    right: 42px; top: 17px;
    margin: 0;
    color: var(--card-white);
    font-size: 31px;
    font-weight: 700;
    letter-spacing: 0.3px;
  }
  .tagline-band {
    position: absolute;
    left: 0; top: 72px;
    width: 100%; height: 38px;
    background: var(--band-grey);
  }
  .tagline {
    position: absolute;
    right: 42px; top: 7px;
    margin: 0;
    color: var(--ink-blue);
    font-size: 20px;
    font-style: italic;
    font-weight: 700;
  }
  .person {
    position: absolute;
    left: 60px; top: 170px;
    display: flex;
    align-items: center;
    gap: 20px;
  }
  .person-mark {
    width: 62px; height: 62px;
    border-radius: 50%;
    background: var(--ink-blue);
    flex: none;
  }
  .person-name {
    margin: 0;
    color: var(--ink-blue);
    font-size: 34px;
    font-weight: 700;
    line-height: 1.1;
  }
  .person-role {
    margin: 2px 0 0;
    color: var(--ink-blue);
    font-size: 15px;
    font-weight: 600;
    letter-spacing: 1px;
  }
  .contacts {
    position: absolute;
    left: 520px; top: 218px;
    margin: 0; padding: 0;
    list-style: none;
  }
  .contact-row {
    display: flex;
    align-items: center;
    gap: 16px;
    height: 42px;
    color: var(--ink-blue);
    font-size: 20px;
  }
  .contact-icon {
    width: 24px; height: 24px;
    flex: none;
  }
  .service-band {
    position: absolute;
    left: 0; bottom: 0;
    width: 100%; height: 86px;
    background: var(--ink-blue-deep);
    display: flex;
    align-items: center;
    justify-content: center;
    gap: 28px;
  }
  .service-rule {
    width: 150px;
    height: 2px;
    background: var(--card-white);
  }
  .service-name {
    margin: 0;
    color: var(--card-white);
    font-size: 22px;
    font-style: italic;
    font-weight: 700;
  }
</style>
</head>
<body>
  <main class="card">
    <header class="brand-band">
      <h1 class="brand-name">Larkspur Yield Advisory</h1>
    </header>
    <div class="tagline-band">
      <p class="tagline">Improving Business Profitibility</p>
    </div>

    <section class="person">
      <span class="person-mark"></span>
      <div>
        <h2 class="person-name">Gordon R Haskel</h2>
        <p class="person-role">DIRECTOR</p>
      </div>
    </section>

    <ul class="contacts">
      <li class="contact-row">
        <svg class="contact-icon" viewBox="0 0 24 24" aria-hidden="true">
          <path fill="#1d73c4" d="M3 8c0-2 2-4 9-4s9 2 9 4v2h-5V8H8v2H3z"/>
          <path fill="#1d73c4" d="M6 11h12l2 8H4z"/>
          <circle cx="12" cy="15" r="2.2" fill="#fff"/>
        </svg>
        <span>123 456 789</span>
      </li>
      <li class="contact-row">
        <svg class="contact-icon" viewBox="0 0 24 24" aria-hidden="true">
          <rect x="2" y="5" width="20" height="14" fill="#1d73c4"/>
          <path d="M2 5l10 8 10-8" fill="none" stroke="#fff" stroke-width="1.6"/>
        </svg>
        <span>email@domainname.com</span>
      </li>
      <li class="contact-row">
        <svg class="contact-icon" viewBox="0 0 24 24" aria-hidden="true">
          <circle cx="12" cy="12" r="10" fill="#1d73c4"/>
          <g fill="none" stroke="#fff" stroke-width="1.3">
            <ellipse cx="12" cy="12" rx="4" ry="10"/>
            <path d="M2 12h20M4 7h16M4 17h16"/>
          </g>
        </svg>
        <span>www.websiteaddress.com</span>
      </li>
    </ul>

    <footer class="service-band">
      <span class="service-rule"></span>
      <p class="service-name">Business Performance Consulting</p>
      <span class="service-rule"></span>
    </footer>
  </main>
</body>
</html>
```